Redesign PixelHarbor's Designer Account Home Page

Are a web designer? New to PixelHarbor? This contest is for you!

We want you to redesign PixelHarbor's designer account home page. We're looking for bold and innovative ideas to make this page a useful and fun experience for you and your fellow designers.

Only new registrants this month are eligible to enter this contest and win prizes.

Your task:
* We want you to put your web design skills to the test and re-design the My Account home page ("Overview") on PixelHarbor to make it more functional and engaging for designers on PixelHarbor.
* The page you are redesigning is here: http://www.pixelharbor-example.com/my-profile.
* Your design should allow for the same functionality as the existing page, though you don't need to replicate the same elements (buttons) or the same menu structure.
* Your design must fit with the branding of the site.
* You must provide a brief outline of what changes you made and why when you upload your design
* 1 submission per designer - make it your best work!
* Pls see "Must haves" for requirements.

Deadline:
* Submit before 12:00am 1st September UTC. Pls convert this deadline to your local timezone and take note of the local time and date

Prizes: $1,000 to win
* First prize for the best design is $700
* Second prize is $200
* Third prize is $100

If you started from scratch, how would you design the MyAccount page on PixelHarbor?

Good luck & have fun!

Mel / The PixelHarbor Team

Target Market(s)

PixelHarbor designers

Number of Pages Required

1 page

Requirements
Must have
• Dimensions: 1200 x 1000 px
• Minimum 150-300 dpi
• Your design must adhere to our quality standards to be eligible to receive a prize
• Submissions must be created in Adobe Creative Suite (Illustrator or Photoshop)
• Your design must fit with the branding of the PixelHarbor site.
• Only new registrants this month are eligible to enter and win prizes.

```html
<!DOCTYPE html>
<html lang="en">
<head>
<meta charset="utf-8">
<title>PixelHarbor – Designer Overview</title>
<link href="https://fonts.googleapis.com/css2?family=Open+Sans:wght@400;600;700;800&display=swap" rel="stylesheet">
<style>
:root{
  --page:#e9eaec;
  --panel:#ffffff;
  --line:#d9dbde;
  --ink:#3a3d42;
  --muted:#8a8e94;
  --dark:#2b2e33;
  --darker:#222428;
  --green:#8cc63f;
  --green-dark:#6fa52b;
  --blue:#2a8fd0;
  --blue-dark:#1f74ad;
  --avatar:#5c6c7e;
}
*{box-sizing:border-box;margin:0;padding:0}
html,body{width:900px;height:1200px;overflow:hidden}
body{font-family:"Open Sans",Arial,sans-serif;background:var(--page);color:var(--ink);font-size:9px;position:relative}
.topbar{height:36px;background:var(--dark);display:flex;align-items:center;padding:0 105px;gap:16px}
.brand{color:#fff;font-weight:700;font-size:15px}
.topnav{display:flex;gap:12px;color:#c8ccd2;font-size:8px}
.topbar .spacer{flex:1}
.profile-menu{background:#3d4148;color:#ddd;padding:4px 10px;font-size:8px;border-radius:2px}
.top-btn{background:var(--green);color:#fff;padding:4px 10px;font-size:8px;border-radius:2px;font-weight:600}
.crumbs{height:30px;background:#f6f6f7;border-bottom:1px solid var(--line);display:flex;align-items:center;padding:0 105px;gap:8px;color:var(--muted);font-size:8px}
.page-title{text-align:center;font-size:24px;font-weight:800;margin:22px 0 14px;color:#33363b}
.wrap{position:absolute;left:105px;top:135px;width:690px}
.sidebar{position:absolute;left:0;top:6px;width:180px}
.browse{background:var(--green);color:#fff;font-weight:700;font-size:13px;padding:9px 12px;border-radius:3px 3px 0 0}
.side-menu{list-style:none;background:var(--panel);border:1px solid var(--line)}
.side-menu li{display:flex;align-items:center;gap:8px;padding:0 10px;height:28px;border-bottom:1px solid #eef0f2;font-size:8.5px;color:#555}
.side-menu li.active{background:#f1f7e8;color:var(--green-dark);font-weight:600}
.side-menu li::before{content:"";width:8px;height:8px;border-radius:2px;background:#b9bec5}
.side-menu li.active::before{background:var(--green)}
.main{position:absolute;left:190px;top:0;width:500px}
.profile-card{background:var(--panel);border:1px solid var(--line);height:210px;display:flex}
.identity{width:190px;text-align:center;padding-top:14px}
.avatar{width:80px;height:90px;margin:0 auto;background:var(--avatar);border:4px solid #fff;outline:1px solid var(--line)}
.name{font-size:18px;font-weight:800;margin-top:8px;color:#2d3035}
.role{color:var(--muted);font-size:8px;margin-top:2px}
.dots{display:flex;justify-content:center;gap:5px;margin-top:10px}
.dots span{width:6px;height:6px;border-radius:50%;background:#c9cdd2}
.dots span.on{background:var(--blue)}
.stats{flex:1;display:grid;grid-template-columns:1fr 1fr;border-left:1px solid var(--line)}
.stat{border-bottom:1px solid var(--line);border-right:1px solid var(--line);padding:8px 10px;display:flex;align-items:center;gap:8px;height:52px}
.stat:nth-child(2n){border-right:none}
.stat.rank{background:var(--blue);color:#fff}
.stat b{font-size:14px;font-weight:800}
.stat small{font-size:7.5px;color:var(--muted);line-height:1.3}
.stat.rank small{color:#d8ebf8}
.badge{width:22px;height:22px;border-radius:50%;background:#cfd4da;flex:none}
.badge.blue{background:var(--blue)}
.section-title{font-size:15px;font-weight:800;margin:20px 0 6px;color:#2f3237}
.getting{background:var(--panel);border:1px solid var(--line);display:grid;grid-template-columns:1fr 1fr}
.task{height:27px;border-bottom:1px solid #eef0f2;display:flex;align-items:center;gap:7px;padding:0 10px;font-size:8px;color:#666}
.getting .col:first-child{border-right:1px solid var(--line)}
.task .box{width:9px;height:9px;border:1px solid #bbb;border-radius:2px;flex:none}
.task.done .box{background:var(--green);border-color:var(--green)}
.progress{flex:1;height:9px;background:#e3e6ea;border-radius:5px;overflow:hidden}
.progress i{display:block;width:25%;height:100%;background:var(--blue)}
.sub{font-size:8px;color:var(--muted);margin:-2px 0 8px}
.jobs{background:var(--panel);border:1px solid var(--line)}
.job{height:33px;display:flex;align-items:center;gap:10px;padding:0 10px;border-bottom:1px solid #eef0f2}
.job-icon{width:20px;height:20px;border-radius:50%;background:var(--blue);flex:none}
.job-title{flex:1;color:var(--blue-dark);font-weight:600;font-size:8.5px}
.job-details{color:var(--muted);font-size:7.5px}
.watch{background:var(--blue);color:#fff;font-size:7.5px;padding:4px 9px;border-radius:2px;font-weight:600}
.footer{position:absolute;left:0;top:856px;width:900px;height:344px;background:var(--dark);color:#b4b9c0}
.footer-cols{position:absolute;left:105px;top:26px;width:690px;display:flex;gap:26px}
.fcol h4{color:#fff;font-size:11px;font-weight:700;margin-bottom:8px}
.fcol ul{list-style:none}
.fcol li{font-size:7.5px;line-height:15px}
.tags{display:flex;flex-wrap:wrap;gap:4px;width:130px}
.tags span{border:1px solid #50555d;padding:2px 5px;font-size:7px}
.newsletter input{width:150px;height:20px;border:none;border-radius:2px;background:#fff;margin:2px 0 10px;font:inherit}
.icon-row{display:flex;gap:6px;margin-bottom:8px}
.icon-row span{width:14px;height:14px;border-radius:50%;background:#6b7079}
.flag-row{display:flex;gap:6px;margin-bottom:6px}
.flag-row span{width:16px;height:11px;background:#6b7079}
.foot-brand{color:#fff;font-weight:700;font-size:14px;margin-top:8px}
.copyright{position:absolute;left:0;bottom:0;width:900px;height:30px;background:var(--darker);display:flex;align-items:center;justify-content:center;font-size:7px;color:#7d828a}
</style>
</head>
<body>
<header class="topbar">
  <div class="brand">PixelHarbor</div>
  <nav class="topnav"><span>Categories</span><span>Designers</span><span>Browse Jobs</span><span>How it works</span></nav>
  <div class="spacer"></div>
  <div class="profile-menu">My Profile ▾</div>
  <div class="top-btn">Post a Job</div>
</header>
<div class="crumbs"><span>Home</span><span>›</span><span>My Profile</span></div>
<h1 class="page-title">Overview</h1>

<div class="wrap">
  <aside class="sidebar">
    <div class="browse">Browse Jobs</div>
    <ul class="side-menu">
      <li class="active">Overview</li>
      <li>Notifications</li>
      <li>Invites</li>
      <li>Submissions</li>
      <li>Messages</li>
      <li>Watchlist</li>
      <li>Badges</li>
      <li>My Profile</li>
    </ul>
  </aside>

  <main class="main">
    <section class="profile-card">
      <div class="identity">
        <div class="avatar" role="img" aria-label="Designer profile photo placeholder"></div>
        <div class="name">Your Name</div>
        <div class="role">Member · Level 1</div>
        <div class="dots"><span></span><span class="on"></span><span></span><span></span></div>
      </div>
      <div class="stats">
        <div class="stat rank"><div><small>Rank<br>Designer Rank</small></div><b>435699</b></div>
        <div class="stat"><span class="badge"></span><small>Top 1000 Designer</small></div>
        <div class="stat"><b>0</b><small>Contests won</small></div>
        <div class="stat"><span class="badge"></span><small>Top 5% of active designers</small></div>
        <div class="stat"><b>$0.00</b><small>Total earnings</small></div>
        <div class="stat"><span class="badge blue"></span><small>Details</small></div>
        <div class="stat" style="border-bottom:none"><b>$0.00</b><small>Pending payout</small></div>
        <div class="stat" style="border-bottom:none"></div>
      </div>
    </section>

    <h2 class="section-title">Getting Started</h2>
    <section class="getting">
      <div class="col">
        <div class="task"><span style="font-weight:600">25% complete</span><div class="progress"><i></i></div></div>
        <div class="task done"><span class="box"></span>Verify your email address</div>
        <div class="task done"><span class="box"></span>Upload a profile photo</div>
        <div class="task"><span class="box"></span>Add your first portfolio item</div>
        <div class="task" style="border-bottom:none"><span class="box"></span>Read the design brief guide</div>
      </div>
      <div class="col">
        <div class="task"><span class="box"></span>Add your qualifications</div>
        <div class="task"><span class="box"></span>Write a short bio about your work</div>
        <div class="task"><span class="box"></span>Browse open jobs and add to watchlist</div>
        <div class="task"><span class="box"></span>Set up your payment details</div>
        <div class="task" style="border-bottom:none"><span class="box"></span>Submit your first design</div>
      </div>
    </section>

    <h2 class="section-title" style="margin-top:18px">Recommended Jobs</h2>
    <p class="sub">There are now 12000 jobs waiting for you, browse them and find one to win your first prize.</p>
    <section class="jobs">
      <div class="job"><span class="job-icon"></span><span class="job-title">Modern logo for a boutique coffee roaster opening its second store</span><span class="job-details">Details</span><span class="watch">+ Add to Watchlist</span></div>
      <div class="job"><span class="job-icon"></span><span class="job-title">Landing page refresh for a small fitness studio</span><span class="job-details">Details</span><span class="watch">+ Add to Watchlist</span></div>
      <div class="job"><span class="job-icon"></span><span class="job-title">Label set for a pet accessory range</span><span class="job-details">Details</span><span class="watch">+ Add to Watchlist</span></div>
      <div class="job"><span class="job-icon"></span><span class="job-title">Logo design for a local bakery with a friendly, warm feel</span><span class="job-details">Details</span><span class="watch">+ Add to Watchlist</span></div>
      <div class="job"><span class="job-icon"></span><span class="job-title">New logo for a harbour sailing club</span><span class="job-details">Details</span><span class="watch">+ Add to Watchlist</span></div>
      <div class="job"><span class="job-icon"></span><span class="job-title">T-shirt design for a charity fun run</span><span class="job-details">Details</span><span class="watch">+ Add to Watchlist</span></div>
      <div class="job" style="border-bottom:none"><span class="job-icon"></span><span class="job-title">Business card design for a travel startup</span><span class="job-details">Details</span><span class="watch">+ Add to Watchlist</span></div>
    </section>
  </main>
</div>

<footer class="footer">
  <div class="footer-cols">
    <div class="fcol"><h4>I need a...</h4><ul><li>Logo design</li><li>Web design</li><li>Business card</li><li>Brochure design</li><li>Flyer design</li><li>Banner ad</li><li>Packaging</li><li>T-shirt design</li></ul></div>
    <div class="fcol"><h4>Find a...</h4><ul><li>Logo designer</li><li>Web designer</li><li>Graphic designer</li><li>Illustrator</li><li>Print designer</li><li>Freelancer</li></ul></div>
    <div class="fcol"><h4>About us</h4><ul><li>How it works</li><li>Our team</li><li>Careers</li><li>Press</li><li>Blog</li><li>Contact us</li><li>Help</li></ul></div>
    <div class="fcol"><h4>Popular pages</h4><div class="tags"><span>Logos</span><span>Websites</span><span>Cards</span><span>Icons</span><span>Print</span><span>Flyers</span><span>Posters</span><span>Apps</span><span>Shirts</span></div></div>
    <div class="fcol newsletter"><h4>Subscribe to our newsletter</h4><input type="text" aria-label="Email address">
      <div class="icon-row"><span></span><span></span><span></span><span></span><span></span></div>
      <div class="flag-row"><span></span><span></span><span></span><span></span></div>
      <div class="flag-row"><span></span><span></span><span></span><span></span></div>
      <div class="foot-brand">PixelHarbor</div>
    </div>
  </div>
  <div class="copyright">© 2012 PixelHarbor. All rights reserved. · Terms · Privacy</div>
</footer>
</body>
</html>
```